BrightLoft Cleaning Services - inviting website needed to gain residential and commercial clients

Hello! I need a website for a newly created company that specializes in residential and commercial cleaning services. We clean homes, apartments, condos, rental apt for people that are too busy or don't want to spend time cleaning when they can be doing other things - whether that's because of long working hours or a business family schedule or perhaps for seniors that find it challenging to clean their homes.
In addition, for businesses we offer cleaning services of offices, doctors/dentist offices, essentially any business.
The company name is BrightLoft Cleaning Services which means we offer cleaning services not just inside homes and business but also outside. The outside services we offer include lawn mowing, pressure washing and snow removal.
I'm looking for a clean, contemporary design.
We are environmentally continuous and therefore use products that are not harmful to the environment, people or pets.
I should also mention that I would like to offer booking pages on the site as well so that clients can schedule their cleans and pay on line via credit card.
Website copy to be provided shortly but am hoping to see the initial design concept first?? Or if it helps, I can send copy in a few days

```html
<!DOCTYPE html>
<html lang="en">
<head>
<meta charset="utf-8">
<title>BrightLoft Cleaning Services</title>
<link href="https://fonts.googleapis.com/css2?family=Teko:wght@400;500;600&family=Lato:wght@400;700&display=swap" rel="stylesheet">
<style>
:root{
  --navy:#123a8c;
  --navy-deep:#0f2f78;
  --blue:#1d55c9;
  --sky:#27a9ec;
  --grey-tile:#b9bcc1;
  --page:#eef0f3;
  --ink:#1c2333;
  --muted:#6b7280;
  --star:#f29a1f;
  --white:#ffffff;
}
*{box-sizing:border-box;margin:0;padding:0}
html,body{width:1200px;height:2826px;overflow:hidden}
body{position:relative;background:var(--page);font-family:"Lato",sans-serif;color:var(--ink)}
.abs{position:absolute}
.heading{font-family:"Teko",sans-serif;font-weight:500;color:var(--navy);line-height:1}

/* hero */
.hero{left:0;top:0;width:1200px;height:452px;background:linear-gradient(100deg,#d9dfe4 0%,#eef1ef 35%,#dfe6d9 60%,#cfd8c7 100%)}
.brand{left:249px;top:40px;display:flex;align-items:center;gap:10px}
.brand-dot{width:30px;height:30px;border-radius:50%;background:var(--navy);flex:none}
.brand-name{font-family:"Teko",sans-serif;font-weight:500;font-size:24px;color:var(--navy);line-height:22px}
.offer-btn{left:799px;top:24px;width:152px;height:27px;background:var(--navy);color:var(--white);font-family:"Teko",sans-serif;font-size:17px;display:flex;align-items:center;padding-left:14px}
.nav{left:599px;top:64px;width:352px;display:flex;justify-content:space-between;font-family:"Teko",sans-serif;font-size:14px;color:var(--navy);line-height:1}
.nav a{color:var(--navy);text-decoration:none}
.nav a.current{font-weight:600}
.hero-title{left:249px;top:232px;font-family:"Teko",sans-serif;font-weight:600;font-size:38px;line-height:37px;color:var(--white);text-shadow:0 1px 3px rgba(0,0,0,.35)}
.hero-tile{top:235px;width:102px;height:105px;background:rgba(18,58,140,.88);color:var(--white);font-family:"Teko",sans-serif;font-size:16px;display:flex;flex-direction:column;align-items:center;padding-top:14px;gap:8px}
.hero-tile.active{background:var(--blue)}
.hero-tab{top:325px;width:30px;height:30px;border-radius:50%;background:var(--white);border:7px solid var(--navy)}

/* about */
.about-photo{left:249px;top:492px;width:337px;height:233px;background:linear-gradient(135deg,#c9c3bd,#8da7d0 55%,#3d6fc0)}
.about-title{left:616px;top:494px;font-size:28px}
.about-text{left:616px;top:527px;width:335px;font-size:13px;line-height:21px;color:var(--muted)}
.read-btn{left:616px;top:697px;width:102px;height:26px;background:var(--navy);color:var(--white);font-family:"Teko",sans-serif;font-size:15px;display:flex;align-items:center;padding-left:12px}
.read-btn i{position:absolute;right:-18px;top:0;width:26px;height:26px;background:var(--blue)}

/* services */
.section-title{left:0;width:1200px;text-align:center;font-size:46px}
.ghost{font-family:"Teko",sans-serif;font-weight:600;font-size:110px;color:rgba(255,255,255,.75);line-height:1}
.svc{width:230px;height:196px;background:var(--grey-tile);color:var(--white);font-family:"Teko",sans-serif;font-size:19px;display:flex;flex-direction:column;align-items:center;justify-content:flex-end;padding-bottom:22px;gap:18px}
.svc svg{margin-bottom:auto;margin-top:34px}
.svc.featured{background:var(--navy);align-items:flex-start;justify-content:flex-start;padding:22px 18px 0;gap:6px}
.svc.featured svg{margin:0 0 8px}
.svc.featured p{font-family:"Lato",sans-serif;font-size:11px;line-height:16px}
.svc.promo{background:var(--white);border:5px solid var(--navy);color:var(--navy);font-size:23px;line-height:24px;text-align:center;justify-content:center;padding:0 18px}

/* products */
.product{width:224px}
.product-photo{width:224px;height:250px}
.product-name{font-family:"Teko",sans-serif;font-size:16px;color:var(--ink);margin-top:8px;line-height:1}
.stars{color:var(--star);font-size:13px;letter-spacing:1px;line-height:1}
.products-band{left:0;top:1790px;width:1200px;height:267px;background:linear-gradient(90deg,#3c6fb8 0%,#d9dde3 18%,#eceff2 50%,#e2e4e6 82%,#5d6066 100%)}
.more-btn{left:548px;top:1993px;width:106px;height:25px;background:var(--navy);color:var(--white);font-family:"Teko",sans-serif;font-size:14px;display:flex;align-items:center;justify-content:center}

/* map + request */
.map{left:0;top:2057px;width:1200px;height:424px;background:linear-gradient(120deg,#e8ecef 0%,#e3e8e4 45%,#a9d3f2 62%,#e6e9ec 80%,#b6dcf5 100%)}
.request{left:249px;top:2121px;width:280px;height:300px;background:linear-gradient(160deg,var(--navy),#1f4aa6);color:var(--white);padding:20px 30px}
.request h3{font-family:"Teko",sans-serif;font-weight:500;font-size:21px;line-height:1;margin-bottom:26px}
.request .label{font-family:"Teko",sans-serif;font-size:17px;line-height:1}
.request p{font-size:11px;line-height:16px}
.request .row{margin-bottom:14px}
.request hr{border:0;border-top:1px solid rgba(255,255,255,.25);margin:6px 0 20px}

/* footer */
.footer{left:0;top:2481px;width:1200px;height:345px;background:var(--navy-deep);color:var(--white)}
.footer .brand{left:249px;top:80px;width:200px}
.footer .brand-dot{background:var(--white)}
.footer .brand-name{color:var(--white)}
.f-title{font-family:"Teko",sans-serif;font-size:21px;line-height:1}
.f-contact{left:490px;top:57px}
.f-line{display:flex;gap:10px;font-size:11px;line-height:15px;color:#7fb6ff;margin-top:14px}
.f-form{left:674px;top:57px;width:277px}
.field{background:var(--white);height:23px;font-size:9px;color:#777;padding:6px 8px}
.submit{width:66px;height:25px;background:var(--sky);color:var(--white);font-size:10px;display:flex;align-items:center;justify-content:center}
.f-bottom{left:249px;top:298px;width:702px;font-size:9px;color:#d6def0;display:flex;gap:14px}
</style>
</head>
<body>

<!-- hero -->
<div class="abs hero" role="img" aria-label="Photo of cleaners at work in a bright living room and kitchen"></div>
<div class="abs brand"><span class="brand-dot"></span><span class="brand-name">BrightLoft<br>Cleaning Services</span></div>
<div class="abs offer-btn">Offer Cleaning Services</div>
<nav class="abs nav">
  <a class="current" href="#">Home</a><span>•</span><a href="#">About Us</a><span>•</span><a href="#">Services</a><span>•</span><a href="#">Products</a><span>•</span><a href="#">Locations</a><span>•</span><a href="#">Contact Us</a>
</nav>
<h1 class="abs hero-title">We Clean Homes,<br>Apartments, Condos,<br>Rental</h1>

<div class="abs hero-tile" style="left:618px">
  <svg width="40" height="40" viewBox="0 0 40 40" fill="none" stroke="#fff" stroke-width="2"><path d="M5 19 20 6l15 13"/><path d="M9 16v18h22V16"/><rect x="16" y="23" width="8" height="11"/></svg>Home</div>
<div class="abs hero-tile active" style="left:733px">
  <svg width="40" height="40" viewBox="0 0 40 40" fill="none" stroke="#fff" stroke-width="2"><rect x="6" y="9" width="28" height="25"/><path d="M6 16h28M13 5v7M27 5v7M12 22h4M18 22h4M24 22h4M12 28h4M18 28h4"/></svg>Holiday</div>
<div class="abs hero-tile" style="left:848px">
  <svg width="40" height="40" viewBox="0 0 40 40" fill="none" stroke="#fff" stroke-width="2"><path d="M30 6 18 20M14 19l7 7-9 9-7-7z"/></svg>Spring Cleans</div>
<span class="abs hero-tab" style="left:654px"></span>
<span class="abs hero-tab" style="left:769px"></span>
<span class="abs hero-tab" style="left:884px"></span>

<!-- about -->
<div class="abs about-photo" role="img" aria-label="Photo of a cleaner holding a spray bottle and cloth"></div>
<h2 class="abs heading about-title">About Us</h2>
<p class="abs about-text">Lorem Ipsum is simply dummy text of the printing and typesetting industry. Lorem Ipsum has been the industry's standard dummy text ever since the 1500s, when an unknown printer took a galley of type and scrambled it to make a type specimen book. It has survived not only five centuries, but also the leap into electronic typesetting, remaining essentially unchanged.</p>
<div class="abs read-btn">Read More<i></i></div>

<!-- services -->
<div class="abs ghost" style="left:-10px;top:868px">ervices</div>
<div class="abs ghost" style="left:955px;top:868px">Service</div>
<h2 class="abs heading section-title" style="top:782px">Services</h2>

<div class="abs svc" style="left:249px;top:853px">
  <svg width="90" height="80" viewBox="0 0 90 80" fill="none" stroke="#fff" stroke-width="3"><path d="M8 38 45 8l37 30"/><path d="M16 32v42h58V32"/><rect x="38" y="50" width="14" height="24"/><rect x="22" y="44" width="10" height="10"/><rect x="58" y="44" width="10" height="10"/></svg>Home</div>
<div class="abs svc featured" style="left:486px;top:853px">
  <svg width="50" height="50" viewBox="0 0 50 50" fill="none" stroke="#fff" stroke-width="3"><path d="M42 6 24 26M18 24l9 9-13 13-9-9z"/></svg>
  Spring Cleans
  <p>Lorem Ipsum has been the industry's standard dummy text ever since the 1500s, when an unknown printer took a</p></div>
<div class="abs svc" style="left:722px;top:853px">
  <svg width="90" height="80" viewBox="0 0 90 80" fill="none" stroke="#fff" stroke-width="3"><path d="M12 6l12 34"/><path d="M20 40h50l6 16H24z"/><circle cx="30" cy="64" r="8"/><circle cx="68" cy="64" r="8"/></svg>Lawn Mowing</div>
<div class="abs svc" style="left:249px;top:1057px">
  <svg width="90" height="80" viewBox="0 0 90 80" fill="none" stroke="#fff" stroke-width="3"><path d="M38 8v50M52 8v50"/><rect x="32" y="28" width="26" height="30" rx="4"/><path d="M30 58 18 74M60 58l12 16"/></svg>Pressure Washing</div>
<div class="abs svc" style="left:486px;top:1057px">
  <svg width="90" height="80" viewBox="0 0 90 80" fill="none" stroke="#fff" stroke-width="3"><path d="M24 8l10 26"/><rect x="30" y="30" width="34" height="24" rx="3"/><circle cx="40" cy="64" r="9"/><path d="M66 22l6-6M70 30l8-2M62 14l2-8"/></svg>Snow Removal</div>
<div class="abs svc promo" style="left:722px;top:1057px">Buy 4 Platinum Full Service Cleaning and Get 2 Free Online Only</div>

<!-- products -->
<div class="abs products-band" role="img" aria-label="Photo of surface wiping and carpet steam cleaning"></div>
<div class="abs ghost" style="left:-10px;top:1690px">roducts</div>
<div class="abs ghost" style="left:955px;top:1690px">Produc</div>
<h2 class="abs heading section-title" style="top:1284px">Products</h2>

<div class="abs product" style="left:249px;top:1351px"><div class="product-photo" role="img" aria-label="Photo of pressure washing paving" style="background:linear-gradient(135deg,#bfc0bb,#8f8f89)"></div><div class="product-name">COMMERCIAL CLEANS</div><div class="stars">★★★★☆</div></div>
<div class="abs product" style="left:488px;top:1351px"><div class="product-photo" role="img" aria-label="Photo of a holiday home living room" style="background:linear-gradient(135deg,#5a4536,#a9793f 60%,#3b2c22)"></div><div class="product-name">HOLIDAY HOME MANAGEMENT</div><div class="stars">★★★★☆</div></div>
<div class="abs product" style="left:727px;top:1351px"><div class="product-photo" role="img" aria-label="Photo of a clean wooden kitchen" style="background:linear-gradient(135deg,#7a4a28,#c08d57 55%,#6b3f20)"></div><div class="product-name">REGULAR HOME CLEANS</div><div class="stars">★★★★☆</div></div>
<div class="abs product" style="left:249px;top:1664px"><div class="product-photo" role="img" aria-label="Photo of cleaning supplies and spray bottles" style="background:linear-gradient(135deg,#c9d4dc,#4a7fd0 50%,#e3c13a)"></div><div class="product-name">SPRING CLEANS</div><div class="stars">★★★★☆</div></div>
<div class="abs product" style="left:488px;top:1664px"><div class="product-photo" role="img" aria-label="Photo of a modern rental house exterior" style="background:linear-gradient(180deg,#6fa1cf,#e8e8e4 55%,#9b8d78)"></div><div class="product-name">RENT INSPECTION CLEANS</div><div class="stars">★★★★☆</div></div>
<div class="abs product" style="left:727px;top:1664px"><div class="product-photo" role="img" aria-label="Photo of an empty bright kitchen" style="background:linear-gradient(135deg,#f1f1ee,#cfcdc7 60%,#b9a98f)"></div><div class="product-name">VACATE CLEANS</div><div class="stars">★★★★☆</div></div>
<div class="abs more-btn">All More Product</div>

<!-- map + request -->
<div class="abs map" role="img" aria-label="Street map of the service area with location pins"></div>
<div class="abs request">
  <h3>Any Request ?</h3>
  <div class="row"><div class="label">Get in touch !</div><p>ABC Street City 12345</p></div>
  <div class="row"><span class="label">Phone:</span> <span style="font-size:11px">+00 000-0000</span></div>
  <div class="row"><span class="label">Email:</span> <span style="font-size:11px">info@brightloftcleaning.com</span></div>
  <hr>
  <h3 style="margin-bottom:8px">Want to Join the Team ?</h3>
  <p>Lorem Ipsum is simply dummy text of the printing and typesetting industry</p>
</div>

<!-- footer -->
<footer class="abs footer">
  <div class="abs brand"><span class="brand-dot"></span><span class="brand-name">BrightLoft<br>Cleaning Services</span></div>
  <div class="abs f-contact">
    <div class="f-title">Contact Us</div>
    <div class="f-line"><svg width="12" height="16" viewBox="0 0 12 16" fill="#fff"><path d="M6 0a6 6 0 0 0-6 6c0 4.5 6 10 6 10s6-5.5 6-10a6 6 0 0 0-6-6zm0 8.5A2.5 2.5 0 1 1 6 3.5a2.5 2.5 0 0 1 0 5z"/></svg><span>BrightLoft Office<br>215 Maple Row #12<br>Fairview, CA 90210</span></div>
    <div class="f-line"><svg width="13" height="13" viewBox="0 0 24 24" fill="#fff"><path d="M6.6 10.8a15 15 0 0 0 6.6 6.6l2.2-2.2a1 1 0 0 1 1-.25 11.4 11.4 0 0 0 3.6.57 1 1 0 0 1 1 1V20a1 1 0 0 1-1 1A17 17 0 0 1 3 4a1 1 0 0 1 1-1h3.5a1 1 0 0 1 1 1c0 1.25.2 2.45.57 3.57a1 1 0 0 1-.25 1z"/></svg><span>555 014 2297</span></div>
  </div>
  <div class="abs f-form">
    <div class="f-title" style="margin-bottom:8px">Form for requesting more information.</div>
    <div class="field">Contact Name (Required)</div>
    <div style="display:flex;gap:8px;margin-top:9px"><div class="field" style="width:136px">Email (Required)</div><div class="field" style="flex:1">Phone # (optional)</div></div>
    <div class="field" style="height:70px;margin-top:9px">Message</div>
    <div class="submit" style="margin-top:9px">Submit</div>
  </div>
  <div class="abs f-bottom"><span>2018 BrightLoft Cleaning Services. All Rights Reserved.</span><span>|</span><span>Terms of Usage</span><span>|</span><span>Privacy Policy</span></div>
</footer>

</body>
</html>
```